Tarvik Plans - Worpress Design

We are a consultancy to help builders to optimize their planning in order to save building costs. For that reason we need a website to offer our services, present our history, the mission and offer a plug-in for a first contact (including calendar), testimonials, a blog etc.
As an idea, I really like: https://www.fendrowadvisory.de/
Later on the website should be programmed in www.quelvo.de in our Wordpress area. The text, of course, will be done by myself. The colors should be suitable to our recently designed logo.

```html
<!DOCTYPE html>
<html lang="en">
<head>
<meta charset="utf-8">
<title>Tarvik Plans</title>
<link href="https://fonts.googleapis.com/css2?family=Poppins:wght@400;500;600;700&display=swap" rel="stylesheet">
<style>
:root{
  --gold:#c7983d;
  --gold-light:#e9cb85;
  --gold-pale:#f6e7c6;
  --dark:#2a2a2a;
  --text:#333;
  --muted:#555;
  --card:#f8f6f6;
  --grey:#c9c9c9;
}
*{margin:0;padding:0;box-sizing:border-box}
html,body{width:1200px;height:5042px;overflow:hidden;background:#fff}
body{font-family:'Poppins',sans-serif;color:var(--text);position:relative}
.abs{position:absolute}
.wash{position:absolute;background:radial-gradient(ellipse at center,rgba(241,217,166,.8) 0%,rgba(246,229,193,.5) 45%,rgba(255,255,255,0) 72%)}
.brand{display:flex;align-items:center;gap:10px}
.brand-mark{width:34px;height:34px;border:3px solid var(--gold)}
.brand-name{font-weight:600;font-size:20px;color:var(--gold);letter-spacing:1px;text-transform:uppercase;line-height:1}
.brand-tag{font-weight:600;font-size:9px;color:var(--gold);letter-spacing:2px;text-transform:uppercase}
.nav{top:56px;left:466px;display:flex;gap:22px;font-size:15px;color:#333}
.nav a{color:inherit;text-decoration:none}
.nav .active{border-bottom:3px solid var(--gold);padding-bottom:6px}
h1.hero-title{top:222px;left:80px;font-size:48px;font-weight:600;line-height:56px;color:#1e1e1e}
.hero-text{top:424px;left:86px;font-size:14px;line-height:23px;color:#444}
.btn{display:flex;align-items:center;justify-content:space-between;padding:0 22px;width:190px;height:62px;font-size:14px;font-weight:500;text-transform:uppercase;color:#222;border:3px solid var(--gold);background:#fff}
.btn-fill{background:linear-gradient(90deg,#b8892f,#e4c27a);border:none;color:#222}
.btn-dot{width:26px;height:26px;border-radius:50%;background:linear-gradient(135deg,#b8892f,#e6c67e);display:flex;align-items:center;justify-content:center}
.btn-fill .btn-dot{background:transparent;border:2px solid #fff}
.section-title{font-size:40px;font-weight:600;color:#1e1e1e;text-align:center;text-transform:uppercase}
.sub{display:flex;align-items:center;justify-content:center;gap:8px;font-size:24px;font-weight:500;color:var(--gold)}
.sub::before,.sub::after{content:"";width:55px;height:1px;background:var(--gold)}
.para{font-size:15px;line-height:26px;color:#333;text-align:justify}
.service{width:494px;height:240px;background:var(--card)}
.service .icon{position:absolute;left:0;top:0;width:110px;height:110px;background:var(--dark);display:flex;align-items:center;justify-content:center}
.service h3{position:absolute;left:140px;top:34px;font-size:17px;font-weight:600;color:var(--gold);text-transform:uppercase}
.service p{position:absolute;left:140px;top:68px;width:305px;font-size:15px;line-height:26px;text-align:justify}
.read{display:flex;align-items:center;gap:8px;font-size:14px;font-weight:500;color:var(--gold);text-transform:uppercase}
.read i{width:18px;height:18px;border-radius:50%;background:var(--gold);display:inline-block}
.service .read{position:absolute;left:140px;top:187px}
.checks{list-style:none;font-size:17px;line-height:36px}
.checks li{display:flex;align-items:center;gap:14px}
.panel{top:3485px;left:60px;width:1080px;height:410px;background:#fafafa;border-radius:30px}
.testi{width:320px;text-align:center}
.avatar{width:72px;height:72px;border-radius:50%;margin:0 auto;background:linear-gradient(135deg,#6b5a52,#c9b6a8)}
.testi .name{font-size:13px;font-weight:600;margin-top:14px}
.testi .role{font-size:10px;color:#666}
.stars{color:var(--gold);font-size:12px;letter-spacing:2px}
.testi blockquote{font-size:14.5px;line-height:26px;color:#555;margin-top:14px;position:relative}
.q{color:var(--gold);font-size:26px;font-weight:700;line-height:0}
.blog{width:310px;height:460px;background:#fff;box-shadow:0 2px 14px rgba(0,0,0,.08)}
.blog .photo{height:290px;margin:6px}
.blog .date{margin:22px 0 0 26px;font-size:10px;color:var(--gold);display:flex;gap:8px;align-items:center}
.blog h4{margin:14px 26px 0;font-size:19px;font-weight:500;line-height:27px;color:#1e1e1e}
.blog .read{margin:12px 0 0 26px;text-transform:none;font-size:15px}
footer{top:4712px;left:0;width:1200px;height:264px;background:var(--dark);color:#fff}
.fcontact{display:flex;align-items:center;gap:14px;font-size:14px;line-height:19px}
.ficon{width:32px;height:32px;border-radius:50%;background:linear-gradient(135deg,#b8892f,#e6c67e);display:flex;align-items:center;justify-content:center}
.flinks{top:4904px;left:0;width:1200px;display:flex;justify-content:center;gap:22px;font-size:15px;color:#fff}
.flinks span.sep{color:var(--gold)}
.copy{top:4976px;left:0;width:1200px;height:66px;background:linear-gradient(90deg,#b8892f,#f0d894 55%,#c59a45);display:flex;align-items:center;justify-content:space-between;padding:0 80px;font-size:14px;color:#222}
.social{display:flex;gap:8px}
.social i{width:24px;height:24px;border:2px solid #222;border-radius:50%;display:block}
</style>
</head>
<body>

<div class="wash" style="top:740px;left:940px;width:300px;height:400px" role="img" aria-label="Soft gold decorative shape"></div>
<div class="wash" style="top:1400px;left:-60px;width:300px;height:500px" role="img" aria-label="Soft gold decorative shape"></div>
<div class="wash" style="top:3190px;left:-60px;width:230px;height:430px" role="img" aria-label="Soft gold decorative shape"></div>
<div class="wash" style="top:3910px;left:900px;width:340px;height:420px" role="img" aria-label="Soft gold decorative shape"></div>

<header>
  <div class="abs brand" style="top:38px;left:84px">
    <span class="brand-mark"></span>
    <div><div class="brand-name">Tarvik Plans</div><div class="brand-tag">Planning that pays</div></div>
  </div>
  <nav class="abs nav">
    <a class="active">Home</a><a>Our History</a><a>Services</a><a>Mission</a><a>Testimonials</a><a>Blogs</a><a>Contact</a><a>Offers</a>
  </nav>
</header>

<section class="hero">
  <h1 class="abs hero-title">HOW TO BUILD<br>HOMES FOR<br>THE FUTURE ?</h1>
  <p class="abs hero-text">Sample text. Lorem ipsum dolor<br>sit amet, consectetur adipi</p>
  <div class="abs btn" style="top:514px;left:86px">Know more <span class="btn-dot"><svg width="10" height="10"><path d="M2 5h6M5 2l3 3-3 3" stroke="#fff" stroke-width="1.6" fill="none"/></svg></span></div>
  <div class="abs btn btn-fill" style="top:596px;left:86px">View offers <span class="btn-dot"><svg width="10" height="10"><path d="M3 1l4 4-4 4" stroke="#fff" stroke-width="1.6" fill="none"/></svg></span></div>
  <svg class="abs" style="top:105px;left:452px" width="620" height="645">
    <polygon points="0,640 0,360 320,0 320,40 30,360 30,640" fill="#cfcfcf"/>
    <polygon points="590,640 590,310 360,120 360,90 620,300 620,640" fill="#ead7b0"/>
    <polygon points="40,640 40,370 320,60 350,120 580,330 580,640" fill="url(#heroPh)" role="img" aria-label="Photo: two construction workers in hard hats reviewing plans on a building site"/>
    <defs><linearGradient id="heroPh" x1="0" y1="0" x2="0" y2="1"><stop offset="0" stop-color="#c99a5a"/><stop offset=".6" stop-color="#7b8797"/><stop offset="1" stop-color="#d7cbb7"/></linearGradient></defs>
  </svg>
</section>

<section class="history">
  <svg class="abs" style="top:922px;left:58px" width="590" height="610">
    <circle cx="250" cy="250" r="247" fill="none" stroke="var(--gold)" stroke-width="3"/>
    <circle cx="250" cy="250" r="238" fill="url(#towerPh)" role="img" aria-label="Photo: glass office tower seen from below"/>
    <circle cx="417" cy="443" r="165" fill="#fff"/>
    <circle cx="417" cy="443" r="158" fill="url(#engPh)" role="img" aria-label="Photo: two engineers in hard hats studying blueprints"/>
    <defs>
      <linearGradient id="towerPh" x1="0" y1="0" x2="1" y2="1"><stop offset="0" stop-color="#dfe8f0"/><stop offset=".5" stop-color="#4f6d8f"/><stop offset="1" stop-color="#a9bdd0"/></linearGradient>
      <linearGradient id="engPh" x1="0" y1="0" x2="1" y2="1"><stop offset="0" stop-color="#eef0f2"/><stop offset=".6" stop-color="#cfd4d9"/><stop offset="1" stop-color="#3d4f7a"/></linearGradient>
    </defs>
  </svg>
  <h2 class="abs section-title" style="top:1000px;left:723px;text-align:left">Our History</h2>
  <div class="abs sub" style="top:1060px;left:718px;width:280px">Who We Are</div>
  <p class="abs para" style="top:1157px;left:723px;width:390px">Lorem ipsum dolor sit amet, consefghctetur adipiscing elit, sed do eiusmod tempor incididunt ut labore et dolore magna aliqua. Ut enim ad minim veniam, quis nostrud exercitation ullamco laboris nisi ut</p>
  <p class="abs para" style="top:1310px;left:723px;width:390px">Aliquip ex ea commodo consequat. Duis aute irure dolor in reprehenderit in voluptate velit esse cillum</p>
  <div class="abs btn" style="top:1402px;left:724px">Know more <span class="btn-dot"><svg width="10" height="10"><path d="M2 5h6M5 2l3 3-3 3" stroke="#fff" stroke-width="1.6" fill="none"/></svg></span></div>
</section>

<section class="services">
  <h2 class="abs section-title" style="top:1680px;left:0;width:1200px">Our Services</h2>
  <div class="abs sub" style="top:1735px;left:0;width:1200px">What We Do?</div>

  <div class="abs service" style="top:1867px;left:85px">
    <div class="icon"><svg width="60" height="60" fill="none" stroke="var(--gold)" stroke-width="3"><circle cx="30" cy="32" r="14"/><path d="M30 24v10M30 38v2M30 6v6M10 14l4 4M50 14l-4 4M4 32h6M50 32h6M24 50h12"/></svg></div>
    <h3>Strategy</h3>
    <p>Lorem ipsum dolor sit amet, consef ghctetur adipiscing elit, sed do eiu smod tempor incididunt ut labore et dolore magna aliqua. Ut enim ad minim</p>
    <div class="read">Read more <i></i></div>
  </div>
  <div class="abs service" style="top:1867px;left:620px">
    <div class="icon"><svg width="60" height="60" fill="var(--gold)"><path d="M8 24h10l20-12v36L18 36H8z"/><path d="M14 36l4 14h6l-3-14z"/><path d="M44 22l8-4M44 30h10M44 38l8 4" stroke="var(--gold)" stroke-width="3"/></svg></div>
    <h3>Results</h3>
    <p>Lorem ipsum dolor sit amet, consef ghctetur adipiscing elit, sed do eiu smod tempor incididunt ut labore et dolore magna aliqua. Ut enim ad minim</p>
    <div class="read">Read more <i></i></div>
  </div>
  <div class="abs service" style="top:2140px;left:85px">
    <div class="icon"><svg width="64" height="60" fill="var(--gold)"><path d="M14 8h36l12 14L32 54 2 22z"/><path d="M2 22h60M20 8l12 46M44 8L32 54" stroke="var(--dark)" stroke-width="2"/></svg></div>
    <h3>Expertise</h3>
    <p>Lorem ipsum dolor sit amet, consef ghctetur adipiscing elit, sed do eiu smod tempor incididunt ut labore et dolore magna aliqua. Ut enim ad minim</p>
    <div class="read">Read more <i></i></div>
  </div>
  <div class="abs service" style="top:2140px;left:620px">
    <div class="icon"><svg width="70" height="60" fill="var(--gold)"><circle cx="22" cy="20" r="10"/><circle cx="46" cy="20" r="10"/><path d="M4 50c0-14 8-20 18-20s18 6 18 20zM30 50c0-14 6-20 16-20s18 6 18 20z"/></svg></div>
    <h3>Support</h3>
    <p>Lorem ipsum dolor sit amet, consef ghctetur adipiscing elit, sed do eiu smod tempor incididunt ut labore et dolore magna aliqua. Ut enim ad minim</p>
    <div class="read">Read more <i></i></div>
  </div>
</section>

<section class="mission">
  <h2 class="abs section-title" style="top:2648px;left:93px;text-align:left">Our Mission</h2>
  <div class="abs sub" style="top:2706px;left:85px;width:290px">Task&nbsp; We Do</div>
  <p class="abs para" style="top:2777px;left:85px;width:398px">Lorem ipsum dolor sit amet, consefghctetur adipiscing elit, sed do eiusmod tempor incididunt ut labore et dolore magna aliqua. Ut enim ad minim veniam, quis nostrud exercitation ullamco laboris nisi ut</p>
  <ul class="abs checks" style="top:2930px;left:85px">
    <li><svg width="18" height="18" fill="none" stroke="var(--gold)" stroke-width="2"><rect x="1" y="3" width="14" height="14"/><path d="M4 9l4 4 9-11"/></svg>Branding Strategy</li>
    <li><svg width="18" height="18" fill="none" stroke="var(--gold)" stroke-width="2"><rect x="1" y="3" width="14" height="14"/><path d="M4 9l4 4 9-11"/></svg>Excellence in Quality</li>
    <li><svg width="18" height="18" fill="none" stroke="var(--gold)" stroke-width="2"><rect x="1" y="3" width="14" height="14"/><path d="M4 9l4 4 9-11"/></svg>Pre Eminent Providers</li>
    <li><svg width="18" height="18" fill="none" stroke="var(--gold)" stroke-width="2"><rect x="1" y="3" width="14" height="14"/><path d="M4 9l4 4 9-11"/></svg>Time Management</li>
  </ul>
  <svg class="abs" style="top:2482px;left:572px" width="620" height="640">
    <polygon points="0,638 0,360 320,0 320,40 24,360 24,638" fill="#cfcfcf"/>
    <polygon points="590,638 590,300 360,140 360,110 615,290 615,638" fill="#ead7b0"/>
    <polygon points="40,638 40,370 320,60 350,140 580,300 580,638" fill="url(#meetPh)" role="img" aria-label="Photo: two colleagues discussing work at a laptop"/>
    <defs><linearGradient id="meetPh" x1="0" y1="0" x2="1" y2="1"><stop offset="0" stop-color="#c7c4c0"/><stop offset=".5" stop-color="#6d6a6c"/><stop offset="1" stop-color="#b79a7c"/></linearGradient></defs>
  </svg>
</section>

<section class="testimonials">
  <h2 class="abs section-title" style="top:3318px;left:0;width:1200px">What Our Clients Say</h2>
  <div class="abs sub" style="top:3372px;left:0;width:1200px">Testimonials</div>
  <div class="abs panel"></div>
  <div class="abs testi" style="top:3585px;left:94px">
    <div class="avatar" role="img" aria-label="Client portrait"></div>
    <div class="name">Mara Vellin</div><div class="role">CEO, Corvane Ltd.</div><div class="stars">★★★★★</div>
    <blockquote><span class="q">“</span> Lorem ipsum dolor sit amet, cov nsectetur adipiscing elit. Cras nec libero gravida lacus consectetur <span class="q">„</span></blockquote>
  </div>
  <div class="abs testi" style="top:3585px;left:440px">
    <div class="avatar" role="img" aria-label="Client portrait"></div>
    <div class="name">Mara Vellin</div><div class="role">CEO, Corvane Ltd.</div><div class="stars">★★★★★</div>
    <blockquote><span class="q">“</span> Lorem ipsum dolor sit amet, cov nsectetur adipiscing elit. Cras nec libero gravida lacus cons <span class="q">„</span></blockquote>
  </div>
  <div class="abs testi" style="top:3585px;left:802px">
    <div class="avatar" role="img" aria-label="Client portrait"></div>
    <div class="name">Mara Vellin</div><div class="role">CEO, Corvane Ltd.</div><div class="stars">★★★★★</div>
    <blockquote><span class="q">“</span> Lorem ipsum dolor sit amet, cov nsectetur adipiscing elit. Cras nec libero gravida lacus consectetur <span class="q">„</span></blockquote>
  </div>
</section>

<section class="blog-list">
  <h2 class="abs section-title" style="top:3998px;left:0;width:1200px">Our Blog</h2>
  <div class="abs sub" style="top:4055px;left:0;width:1200px">Latest News</div>
  <article class="abs blog" style="top:4165px;left:80px">
    <div class="photo" role="img" aria-label="Photo: team meeting in a bright office" style="background:linear-gradient(135deg,#e9e9e9,#9a948e)"></div>
    <div class="date">▣ FEB 20, 2023</div>
    <h4>Lorum ipsum dolor sit solicit amet consequet</h4>
    <div class="read">Read More <i></i></div>
  </article>
  <article class="abs blog" style="top:4165px;left:443px">
    <div class="photo" role="img" aria-label="Photo: modern house with blue sky" style="background:linear-gradient(180deg,#3f78c4,#c9c7c0 60%,#8c7a62)"></div>
    <div class="date">▣ FEB 20, 2023</div>
    <h4>Lorum ipsum dolor sit solicit amet consequet</h4>
    <div class="read">Read More <i></i></div>
  </article>
  <article class="abs blog" style="top:4165px;left:800px">
    <div class="photo" role="img" aria-label="Photo: two business people holding a notebook" style="background:linear-gradient(135deg,#d9d5cf,#3b3b42 60%,#e8e3dc)"></div>
    <div class="date">▣ FEB 20, 2023</div>
    <h4>Lorum ipsum dolor sit solicit amet consequet</h4>
    <div class="read">Read More <i></i></div>
  </article>
</section>

<footer class="abs">
  <div class="abs brand" style="top:92px;left:85px">
    <span class="brand-mark"></span>
    <div><div class="brand-name" style="font-size:24px">Tarvik Plans</div><div class="brand-tag" style="font-size:10px">Planning that pays</div></div>
  </div>
  <div class="abs fcontact" style="top:92px;left:392px"><span class="ficon"><svg width="16" height="16" fill="#fff"><path d="M3 1l3 0 1 4-2 1c1 2 3 4 5 5l1-2 4 1v3c0 1-1 2-2 2C7 15 1 9 1 3c0-1 1-2 2-2z"/></svg></span><div>+49 301 555 0190<br>+49 301 555 0191</div></div>
  <div class="abs fcontact" style="top:90px;left:652px"><span class="ficon"><svg width="14" height="18" fill="#fff"><path d="M7 0a6 6 0 0 1 6 6c0 5-6 12-6 12S1 11 1 6a6 6 0 0 1 6-6z"/><circle cx="7" cy="6" r="2" fill="#c7983d"/></svg></span><div>Sample street 12<br>Pin: 10115</div></div>
  <div class="abs fcontact" style="top:96px;left:933px"><span class="ficon"><svg width="16" height="12" fill="none" stroke="#fff" stroke-width="1.6"><rect x="1" y="1" width="14" height="10"/><path d="M1 1l7 6 7-6"/></svg></span><div>hello@tarvikplans.de</div></div>
</footer>
<div class="abs flinks">Our History <span class="sep">|</span> Services <span class="sep">|</span> Mission <span class="sep">|</span> Testimonials <span class="sep">|</span> Blogs <span class="sep">|</span> Contact <span class="sep">|</span> Offers</div>
<div class="abs copy"><span>Copyright @ 2023 All rights reserved</span><div class="social"><i></i><i></i><i></i><i></i></div></div>

</body>
</html>
```